Postcard Design

Law office.
Details are on the attached pdf file:
NOTE: the following items are to be changed, as follows:
1. price is 799
2. delete "Expires 2-8-13"
3. make "Nevada County's..." into "Northern California's ... "
4. Someplace where it fits nicely, add "Fast, Easy, Done!"
5. Delete "no obligation first visit"
6. That attached pdf was a successful ad so I want to maintain that look GENERALLY, but I'm not stuck on anything in particular. Some freedom to play with it for a perfect ad.
7. I'll attach the revised picture and the logo.

```html
<!DOCTYPE html>
<html lang="en">
<head>
<meta charset="utf-8">
<title>Law Office of Daniel R Moreno – Postcard</title>
<link href="https://fonts.googleapis.com/css2?family=Roboto+Condensed:wght@400;700&family=Lato:wght@400;700&family=Arimo:wght@400;700&display=swap" rel="stylesheet">
<style>
  :root{
    --bg:#e6e6e6;
    --white:#ffffff;
    --green:#6b8431;
    --brown:#5a2812;
    --brown-light:#7d3d1c;
    --tan:#e4dba8;
    --tan-text:#e8dca0;
    --ink:#474747;
    --ink-dark:#2b2b2b;
    --rule:#555555;
  }
  html,body{margin:0;padding:0;width:1200px;height:1128px;overflow:hidden;background:var(--bg);}
  .postcard{
    position:absolute;left:40px;top:160px;width:672px;height:485px;
    transform:scale(1.6667);transform-origin:0 0;
    background:var(--white);overflow:hidden;
    font-family:"Roboto Condensed",Arial,sans-serif;
  }
  .postcard-shapes{position:absolute;left:0;top:0;width:672px;height:485px;}
  .txt{position:absolute;margin:0;white-space:nowrap;line-height:1;}
  .headline{left:16px;top:19px;font-size:27px;font-weight:700;color:var(--green);letter-spacing:.2px;}
  .subline{left:16px;font-family:Arimo,Arial,sans-serif;font-size:13.6px;color:var(--ink);}
  .subline--one{top:55px;}
  .subline--two{top:78px;color:var(--green);}
  .value{left:14px;top:137px;font-family:Arimo,Arial,sans-serif;font-size:25px;color:var(--white);}
  .value strong{color:var(--tan-text);}
  .protect{left:14px;top:183px;font-size:24px;font-weight:700;color:var(--white);}
  .easy{left:14px;top:213px;font-size:29px;font-weight:700;color:var(--white);}
  .easy span{color:var(--tan-text);font-family:Arimo,Arial,sans-serif;font-weight:700;}
  .phone{left:14px;top:278px;font-family:Arimo,Arial,sans-serif;font-size:28px;font-weight:700;color:var(--ink-dark);}
  .price-label{left:123px;top:371px;transform:translateX(-50%);font-family:Arimo,Arial,sans-serif;font-size:27px;color:var(--white);}
  .price-value{left:123px;top:403px;transform:translateX(-50%);font-family:Arimo,Arial,sans-serif;font-size:27px;font-weight:700;color:var(--tan-text);}
  .office{left:376px;top:271px;font-size:55px;font-weight:700;color:var(--ink);letter-spacing:.5px;}
  .office-name{left:376px;top:337px;font-family:Arimo,Arial,sans-serif;font-size:21px;color:var(--green);}
  .perks{position:absolute;left:376px;top:380px;margin:0;padding:0;list-style:none;font-family:Lato,Arial,sans-serif;font-size:14.5px;color:var(--ink-dark);}
  .perks li{position:relative;padding-left:16px;margin-bottom:5px;}
  .perks li::before{content:"";position:absolute;left:2px;top:6px;width:6px;height:6px;border-radius:50%;background:var(--green);}
  .perks b{font-weight:700;}
  .brand{position:absolute;left:578px;top:391px;display:flex;align-items:center;gap:5px;font-family:Lato,Arial,sans-serif;font-size:13px;font-weight:700;color:var(--ink-dark);}
  .brand-square{width:10px;height:10px;background:var(--ink-dark);}
  .web{left:505px;top:458px;transform:translateX(-50%);font-family:Lato,Arial,sans-serif;font-size:13.5px;color:var(--white);}
  .web b{color:var(--tan-text);}
</style>
</head>
<body>
<div class="postcard">
  <svg class="postcard-shapes" viewBox="0 0 672 485" xmlns="http://www.w3.org/2000/svg">
    <defs>
      <linearGradient id="brownBand" x1="0" y1="0" x2="1" y2="0">
        <stop offset="0" stop-color="var(--brown)"/>
        <stop offset="0.55" stop-color="var(--brown-light)"/>
        <stop offset="1" stop-color="var(--brown)"/>
      </linearGradient>
      <radialGradient id="sealFill" cx="0.5" cy="0.45" r="0.6">
        <stop offset="0" stop-color="var(--brown-light)"/>
        <stop offset="1" stop-color="var(--brown)"/>
      </radialGradient>
      <linearGradient id="photoTone" x1="0" y1="0" x2="1" y2="1">
        <stop offset="0" stop-color="#ffffff"/>
        <stop offset="0.45" stop-color="#efe2c0"/>
        <stop offset="0.75" stop-color="#c9a24d"/>
        <stop offset="1" stop-color="#8a5a30"/>
      </linearGradient>
    </defs>
    <g role="img" aria-label="Photo of brass scales of justice, an open law book and a wooden gavel">
      <polygon points="364,0 672,0 672,250 406,250" fill="url(#photoTone)"/>
    </g>
    <polygon class="divider" points="350,0 362,0 410,262 398,262" fill="var(--green)"/>
    <rect class="photo-base" x="400" y="250" width="272" height="12" fill="var(--green)"/>
    <rect class="rule" x="0" y="262" width="672" height="5" fill="var(--rule)"/>
    <rect class="headline-rule" x="0" y="113" width="345" height="5" fill="var(--green)"/>
    <polygon class="value-band" points="0,118 345,118 370,262 0,262" fill="url(#brownBand)"/>
    <polygon class="lower-panel" points="0,267 362,267 300,485 0,485" fill="var(--green)"/>
    <polygon class="phone-tab" points="0,268 266,268 240,312 0,312" fill="var(--tan)"/>
    <polygon class="web-bar" points="300,445 672,445 672,485 289,485" fill="var(--brown)"/>
    <circle class="seal-teeth" cx="123" cy="394" r="58" fill="none" stroke="var(--brown)" stroke-width="8" stroke-dasharray="4.5 3.1"/>
    <circle class="seal" cx="123" cy="394" r="55" fill="url(#sealFill)" stroke="var(--tan)" stroke-width="2"/>
  </svg>

  <h1 class="txt headline">NORTHERN CALIFORNIA'S</h1>
  <p class="txt subline subline--one">BEST IN ESTATE PLANS LIVING TRUSTS</p>
  <p class="txt subline subline--two">WILLS &amp; ALL NECESSARY DOCUMENTS</p>

  <p class="txt value">OVER <strong>$2,000</strong> VALUE</p>
  <p class="txt protect">PROTECT YOUR LOVED ONES!</p>
  <p class="txt easy">IT'S EASY <span>Call Now!</span></p>

  <p class="txt phone">916-555-0142</p>
  <p class="txt price-label">Price</p>
  <p class="txt price-value">$799</p>

  <h2 class="txt office">LAW OFFICE</h2>
  <p class="txt office-name">OF DANIEL R MORENO</p>
  <ul class="perks">
    <li><b>Free</b> Notarization</li>
    <li><b>Fast, Easy, Done!</b></li>
  </ul>
  <div class="brand"><span class="brand-square"></span>Moreno</div>

  <p class="txt web"><b>check me out</b> at www.danielmorenolaw.com</p>
</div>
</body>
</html>
```